School Website

I need a design for a School (2 sections: Primary 6-12 years and Secondary 12-18 years). The first page is just a choice of the 2 sections. After we'll need 2 websites (with the same structure: Menu, ...) but with different colors. In fact, we need for end of October, 6 design of school website. So the best websites are going to be made available to you in the future (in pixmarketo) but privately.

Target Market(s)

Public, Parents, ...

Coding

Coded - Design and coding required

Number of Pages Required

5+ page

Font styles to use
Sans Serif

Colors
34a6d7
85cae6
cee9f5
ffffff

Requirements
Must have
• You can check the old Website: http: / /velmoq.be We need the same pages with the same content. Menu: - HomePage - News and communication (like blog page) - Activities (like blog page, with photo gallery) - Contact (Contact form + maps) - In the main menu, we need a special button to connect to an external Website ( button needs to be different than the other menu items The name of this button is "Parents Area"). The logo of 2 sections are attached. Please use it for the design and the choice of colors.
Nice to have
• This is a web design of other school that we like: https://www.quintel.be

```html
<!DOCTYPE html>
<html lang="fr">
<head>
<meta charset="utf-8">
<title>Athénée Royal de Morvelle</title>
<link rel="stylesheet" href="https://fonts.googleapis.com/css2?family=Bitter:wght@500;600&family=Bree+Serif&family=Merriweather+Sans:wght@400&family=Montserrat:wght@400;500&family=Open+Sans:wght@400;600&display=swap">
<style>
:root{
  --green:#2fcf7f;
  --green-dark:#27b06b;
  --sky-top:#5fb6ea;
  --sky-bottom:#e6f3fb;
  --ink:#1c1c1c;
  --muted:#8a8a8a;
  --title:#6d6d6d;
  --line:#c9c9c9;
  --panel:#40425a;
  --white:#ffffff;
  --nav-bg:#f7f7f7;
}
*{margin:0;padding:0;box-sizing:border-box}
html,body{width:1200px;height:2708px;overflow:hidden}
body{position:relative;background:linear-gradient(180deg,var(--sky-top) 0,#a9d8f3 160px,var(--sky-bottom) 420px,#eef6fb 100%);font-family:"Open Sans",sans-serif;color:var(--ink)}
.abs{position:absolute}
.brand{left:87px;top:30px;height:50px;display:flex;align-items:center;gap:10px}
.brand-mark{width:42px;height:42px;border-radius:50%;background:var(--white)}
.brand-name{font-family:"Open Sans",sans-serif;font-weight:600;font-size:21px;color:var(--white)}
.nav{left:85px;top:122px;width:799px;height:54px;background:var(--nav-bg);display:flex;align-items:center;font-family:"Montserrat",sans-serif;font-size:15px;color:var(--ink)}
.nav span{position:absolute;top:18px}
.parents{left:900px;top:122px;width:215px;height:54px;border-radius:27px;background:var(--green);display:flex;align-items:center;font-family:"Montserrat",sans-serif;font-size:15px;color:var(--white)}
.parents-icon{width:54px;height:54px;border-radius:50%;background:var(--green-dark);display:flex;align-items:center;justify-content:center;margin-right:16px}
.sheet{left:85px;top:192px;width:1030px;height:1760px;background:var(--white)}
.hero{left:98px;top:204px;width:1005px;height:417px;background:linear-gradient(180deg,#b0714f 0%,#8a6a5a 45%,#4a5a7a 75%,#3c3540 100%)}
.hero-title{left:120px;top:522px;font-family:"Bree Serif",serif;font-size:40px;color:var(--green);text-shadow:0 2px 3px rgba(0,0,0,.5)}
.hero-sub{left:120px;top:572px;font-family:"Bree Serif",serif;font-size:26px;color:var(--green);text-shadow:0 2px 3px rgba(0,0,0,.5)}
.info{top:660px;display:flex;gap:14px;align-items:center;font-family:"Merriweather Sans",sans-serif;font-size:15px;line-height:23px;color:var(--ink)}
.vsep{top:650px;width:1px;height:66px;border-left:1px dashed var(--line)}
.green-rule{left:85px;top:743px;width:1030px;height:3px;background:var(--green)}
.section-title{left:85px;width:1030px;top:786px;text-align:center;font-family:"Bitter",serif;font-weight:500;font-size:25px;color:var(--ink)}
.divider{top:826px}
.card{width:303px}
.card-img{width:303px;height:202px}
.card-title{margin-top:21px;font-family:"Open Sans",sans-serif;font-weight:600;font-size:16px;color:var(--title)}
.card-text{margin-top:6px;font-size:13px;line-height:21px;color:var(--muted)}
.card-foot{margin-top:14px;display:flex;justify-content:space-between;align-items:center}
.read{font-family:"Montserrat",sans-serif;font-size:11px;font-weight:500;color:var(--green)}
.date{font-size:10px;color:#555}
.contact{left:85px;top:1952px;width:1030px;height:426px;background:var(--panel);color:var(--white)}
.contact h2{position:absolute;left:32px;top:38px;font-family:"Bitter",serif;font-weight:500;font-size:22px}
.contact .lead{position:absolute;left:32px;top:100px;font-family:"Merriweather Sans",sans-serif;font-size:14px;line-height:24px;width:420px}
.contact .row{position:absolute;left:30px;display:flex;gap:12px;align-items:center;font-family:"Merriweather Sans",sans-serif;font-size:15px}
.badge{position:absolute;left:34px;top:310px;width:91px;height:89px;background:var(--white)}
.label{position:absolute;font-family:"Merriweather Sans",sans-serif;font-size:14px}
.field{position:absolute;background:var(--white);border:1px solid #d8d8d8}
.send{position:absolute;left:500px;top:316px;width:169px;height:40px;background:var(--green);font-family:"Montserrat",sans-serif;font-size:14px;display:flex;align-items:center;justify-content:center}
.map{left:85px;top:2378px;width:1030px;height:276px;background:linear-gradient(135deg,#e9eee3,#dfe9d6 50%,#eceee8)}
.footer{left:0;top:2654px;width:1200px;height:54px;background:var(--green);color:var(--white);font-size:14px}
.social{position:absolute;top:13px;width:28px;height:28px;border-radius:50%;background:var(--white);opacity:.9}
</style>
</head>
<body>

<div class="abs brand"><span class="brand-mark"></span><span class="brand-name">Athénée Royal de Morvelle</span></div>

<nav class="abs nav">
  <span style="left:25px">HOME</span>
  <span style="left:118px">|</span>
  <span style="left:171px">NEWS &amp; COMMUNICATION</span>
  <span style="left:420px">|</span>
  <span style="left:472px">ACTIVITIES</span>
  <span style="left:600px">|</span>
  <span style="left:652px">CONTACT</span>
</nav>
<div class="abs parents">
  <span class="parents-icon"><svg width="28" height="20" viewBox="0 0 28 20"><circle cx="10" cy="5" r="4.5" fill="#fff"/><circle cx="20" cy="6" r="3.5" fill="#fff"/><path d="M1 19c0-6 4-8 9-8s9 2 9 8z" fill="#fff"/><path d="M20 11c4 0 7 2 7 7h-6c0-3-1-5-3-6z" fill="#fff"/></svg></span>PARENTS AREA
</div>

<div class="abs sheet"></div>
<div class="abs hero" role="img" aria-label="Photo of a group of smiling pupils with backpacks in front of the school building"></div>
<div class="abs hero-title">Athénée Royal de Morvelle</div>
<div class="abs hero-sub">Maternelles et Primaires</div>

<div class="abs info" style="left:184px">
  <svg width="36" height="38" viewBox="0 0 36 38"><path d="M18 2a10 10 0 0 0-10 10c0 8 10 19 10 19s10-11 10-19A10 10 0 0 0 18 2z" fill="#2fcf7f"/><circle cx="18" cy="12" r="4" fill="#fff"/><ellipse cx="18" cy="34" rx="15" ry="3" fill="none" stroke="#2fcf7f" stroke-width="2"/></svg>
  <div>Rue Albert Dessart<br>12, 5720 Morvelle, Belgique</div>
</div>
<div class="abs vsep" style="left:451px"></div>
<div class="abs info" style="left:503px">
  <svg width="38" height="38" viewBox="0 0 38 38"><circle cx="19" cy="19" r="16" fill="none" stroke="#2fcf7f" stroke-width="4"/><path d="M19 9v11h8" fill="none" stroke="#2fcf7f" stroke-width="4"/></svg>
  <div>Du lundi au vendredi<br>7h00 – 18h</div>
</div>
<div class="abs vsep" style="left:740px"></div>
<div class="abs info" style="left:774px">
  <svg width="40" height="40" viewBox="0 0 40 40"><path d="M9 4l6 8-4 4c2 5 6 9 11 11l4-4 8 6-4 7C17 35 5 23 3 10z" fill="#2fcf7f"/><path d="M24 6a11 11 0 0 1 10 10M24 12a5 5 0 0 1 5 5" fill="none" stroke="#2fcf7f" stroke-width="3"/></svg>
  <div>Appelez-nous Maintenant<br>+32 81 47 16 39</div>
</div>

<div class="abs green-rule"></div>

<h1 class="abs section-title">NOUVELLES ET COMMUNICATION</h1>
<svg class="abs divider" style="left:451px" width="298" height="6" viewBox="0 0 298 6"><line x1="0" y1="3" x2="298" y2="3" stroke="#cfcfcf"/><circle cx="142" cy="3" r="2.5" fill="#cfcfcf"/><circle cx="154" cy="3" r="2.5" fill="#cfcfcf"/></svg>

<div class="abs card" style="left:112px;top:861px"><div class="card-img" role="img" aria-label="School canteen with long tables" style="background:linear-gradient(160deg,#a6b94a,#8d7a45)"></div><div class="card-title">TITLE HERE</div><div class="card-text">Lorem ipsum dolor sit amet, consecteturing elit, sed do eiusmod tempor incidi dunt ut labore et</div><div class="card-foot"><span class="read">READ MORE</span><span class="date">06, SEP - 2016</span></div></div>
<div class="abs card" style="left:450px;top:861px"><div class="card-img" role="img" aria-label="Pupils raising hands in front of a teacher at the blackboard" style="background:linear-gradient(160deg,#3d6a5c,#8a7868)"></div><div class="card-title">TITLE HERE</div><div class="card-text">Lorem ipsum dolor sit amet, consecteturing elit, sed do eiusmod tempor incidi dunt ut labore et</div><div class="card-foot"><span class="read">READ MORE</span><span class="date">06, SEP - 2016</span></div></div>
<div class="abs card" style="left:782px;top:861px"><div class="card-img" role="img" aria-label="Children drawing together at a desk" style="background:linear-gradient(160deg,#c9a88f,#3b5da0)"></div><div class="card-title">TITLE HERE</div><div class="card-text">Lorem ipsum dolor sit amet, consecteturing elit, sed do eiusmod tempor incidi dunt ut labore et</div><div class="card-foot"><span class="read">READ MORE</span><span class="date">06, SEP - 2016</span></div></div>

<div class="abs card" style="left:112px;top:1214px"><div class="card-img" role="img" aria-label="Pupils running along a school corridor with lockers" style="background:linear-gradient(160deg,#5a6fa8,#b28a7a)"></div><div class="card-title">TITLE HERE</div><div class="card-text">Lorem ipsum dolor sit amet, consecteturing elit, sed do eiusmod tempor incidi dunt ut labore et</div><div class="card-foot"><span class="read">READ MORE</span><span class="date">06, SEP - 2016</span></div></div>
<div class="abs card" style="left:450px;top:1214px"><div class="card-img" role="img" aria-label="Pupils with backpacks climbing school stairs" style="background:linear-gradient(160deg,#e4d9c8,#8e8070)"></div><div class="card-title">TITLE HERE</div><div class="card-text">Lorem ipsum dolor sit amet, consecteturing elit, sed do eiusmod tempor incidi dunt ut labore et</div><div class="card-foot"><span class="read">READ MORE</span><span class="date">06, SEP - 2016</span></div></div>
<div class="abs card" style="left:782px;top:1214px"><div class="card-img" role="img" aria-label="Three smiling children with school bags" style="background:linear-gradient(160deg,#d8c0a8,#6d8fb8)"></div><div class="card-title">TITLE HERE</div><div class="card-text">Lorem ipsum dolor sit amet, consecteturing elit, sed do eiusmod tempor incidi dunt ut labore et</div><div class="card-foot"><span class="read">READ MORE</span><span class="date">06, SEP - 2016</span></div></div>

<div class="abs card" style="left:112px;top:1571px"><div class="card-img" role="img" aria-label="Two boys reading a book together in a colourful classroom" style="background:linear-gradient(160deg,#7cc4e8,#d9443a)"></div><div class="card-title">TITLE HERE</div><div class="card-text">Lorem ipsum dolor sit amet, consecteturing elit, sed do eiusmod tempor incidi dunt ut labore et</div><div class="card-foot"><span class="read">READ MORE</span><span class="date">06, SEP - 2016</span></div></div>
<div class="abs card" style="left:450px;top:1571px"><div class="card-img" role="img" aria-label="Classroom of pupils raising their hands" style="background:linear-gradient(160deg,#e8e2c0,#7a6a5a)"></div><div class="card-title">TITLE HERE</div><div class="card-text">Lorem ipsum dolor sit amet, consecteturing elit, sed do eiusmod tempor incidi dunt ut labore et</div><div class="card-foot"><span class="read">READ MORE</span><span class="date">06, SEP - 2016</span></div></div>
<div class="abs card" style="left:782px;top:1571px"><div class="card-img" role="img" aria-label="Young pupils sitting in front of a whiteboard" style="background:linear-gradient(160deg,#f2eee6,#8a5a3e)"></div><div class="card-title">TITLE HERE</div><div class="card-text">Lorem ipsum dolor sit amet, consecteturing elit, sed do eiusmod tempor incidi dunt ut labore et</div><div class="card-foot"><span class="read">READ MORE</span><span class="date">06, SEP - 2016</span></div></div>

<section class="abs contact">
  <h2>CONTACTEZ-NOUS</h2>
  <svg style="position:absolute;left:32px;top:78px" width="152" height="6" viewBox="0 0 152 6"><line x1="0" y1="3" x2="152" y2="3" stroke="#c9cad4"/><circle cx="67" cy="3" r="2.5" fill="#fff"/><circle cx="80" cy="3" r="2.5" fill="#fff"/></svg>
  <p class="lead">If you have any questions or comments about our services please fill out this form. We would love to hear from you.</p>
  <div class="row" style="top:178px"><svg width="22" height="24" viewBox="0 0 22 24"><path d="M11 1a7 7 0 0 0-7 7c0 6 7 12 7 12s7-6 7-12a7 7 0 0 0-7-7z" fill="none" stroke="#fff" stroke-width="2"/><circle cx="11" cy="8" r="2.5" fill="#fff"/><ellipse cx="11" cy="21" rx="9" ry="2" fill="none" stroke="#fff" stroke-width="1.5"/></svg>Rue Albert Dessart 12, 5720 Morvelle, Belgique</div>
  <div class="row" style="top:221px"><svg width="22" height="22" viewBox="0 0 22 22"><circle cx="11" cy="11" r="9.5" fill="none" stroke="#fff" stroke-width="2"/><path d="M11 5v7h5" fill="none" stroke="#fff" stroke-width="2"/></svg>Du lundi au vendredi 7h00 – 18h</div>
  <div class="row" style="top:263px"><svg width="22" height="22" viewBox="0 0 40 40"><path d="M9 4l6 8-4 4c2 5 6 9 11 11l4-4 8 6-4 7C17 35 5 23 3 10z" fill="none" stroke="#fff" stroke-width="3"/><path d="M24 6a11 11 0 0 1 10 10" fill="none" stroke="#fff" stroke-width="3"/></svg>Appelez-nous Maintenant: +32 81 47 16 39</div>
  <div class="badge"></div>

  <span class="label" style="left:501px;top:43px">Full Name*</span>
  <span class="label" style="left:761px;top:43px">Email *</span>
  <div class="field" style="left:501px;top:62px;width:239px;height:44px"></div>
  <div class="field" style="left:761px;top:62px;width:239px;height:44px"></div>
  <span class="label" style="left:500px;top:132px">Message*</span>
  <div class="field" style="left:500px;top:152px;width:500px;height:144px"></div>
  <div class="send">SEND MESSAGE</div>
</section>

<div class="abs map" role="img" aria-label="Road map of the region with a red marker on the school location"></div>

<footer class="abs footer">
  <span style="position:absolute;left:117px;top:16px">© Copyright 2019 velmoq.be</span>
  <span class="social" style="left:983px"></span>
  <span class="social" style="left:1020px"></span>
  <span class="social" style="left:1057px"></span>
</footer>

</body>
</html>
```